Colourful Bold Design for Pet Insurance Website

PLEASE NOTE THAT THIS PROJECT HAS BEEN EXTENDED. Please read the PROJECT EXTENSION DOCUMENT BEFORE STARTING WORK ON ANY DESIGNS.

We are looking for a colourful bold new template design for our JOOMLA HOMEPAGE and a matching design for our new WORDPRESS BLOG.

The website will help pet owners work out which insurance policy best meets their needs. The aim of the website is to explain policy differences in a plain clear manner.

The website will need to have a professional colourful image. It needs to be BOLD, CLEAN AND SHARP rather than soft, pastel and cuddly.

COLOUR SCHEME
The website needs to have a bold colourful design on a white background.
On the inner pages we will have five different types of policies which will be colour coded. We would ideally therefore like to incorporate five distinct colours in the design. See attached document for example of colour schemes we like.

LOGO
We want to keep the existing logo. Please find the file attached. You may though change the logo colours.

CONTENT
One of the reasons for the new design is that we want to change the style of the homepage and include new content. Our current homepage can be found at www.furrow-cover-polls.co.uk.

Content Required
Slideshow
Article Intro.. About Pet Insurance
Policy Lookup Box (see existing site… you can change the design of this)
Six link options (see links on left of current page)
Latest Reviews (List of 6)
Ad (Same dimensions as currently on homepage)

News and Comment Section - To include Three or Four Articles, Title, Intro to article (probably 3 or 4 lines .. about 400px wide), Read more link
Social Media Section
Social feed Plugin with Feed
Latest Tweets Plugin
Pet Charities Latest Tweets
Footer
Larger footer with lots of links grouped in sections

It does not need to include the clipart pic of the pets which is on the current homepage.

Examples of Websites and Templates We Like
http://www.pawlane.com/ (like colours… fonts…layout)
http://sitetheme.brightkiln.com/?template=upbeat&path=/... (like the clarity, "white" space etc)
http://www.layoutforge.com/demo/51872.html (like white space, clear easy to read fonts… don’t like colour scheme, size of top picture)
http://www.layoutforge.com/website-templates/63915.html (like colour scheme, use of white space)

FEEDBACK
I will provide lots of feedback on all designs submitted so that together we can get the best result.

For clarification this is a DESIGN ONLY project. Our website developer will view the designs before we make our final choice as he wants to ensure he can develop "sharp, practical and most importantly light weight web interface" from the design.

Just updated this brief to clarify design issues, content issues and to give some more examples of site designs I like. 

Please note that although we wish to keep the logo you can change the colours to suit your design. 

Please note that we have now added details of pictures we would be happy to use on the website.  We would prefer it if you used one of these.   Otherwise please ensure your picture includes a nice dog and nice cat and no people!

I have been delighted with the quality of the designs submitted for this project.  So much so that I am going to extend the project to include some additional inner pages.   The amended brief will be posted on here on Friday 10 May.   The deadline will be extended and the budget will also be increased. 

Reason: Additional inner pages now required. Budget will be increased. Revised brief to be posted on here Friday 10 May.

Target Market(s)

Pet owners in the UK who are confused about pet insurance. It therefore needs to be a bold design which is plain, clean and easy to read. It should use bold colours rather than pastels and should not use "cuddly" images.

Industry/Entity Type

Insurance

Requirements
Must have
• Bold clear and distinct colours (preferably 5)
Content as per uploaded file (not just content from existing site)
Easy to read fonts
Should not have
• Pastel colours
Cuddly images

```html
<!DOCTYPE html>
<html lang="en">
<head>
<meta charset="utf-8">
<title>Furrow Cover Polls UK – Home</title>
<link rel="stylesheet" href="https://fonts.googleapis.com/css2?family=Open+Sans:wght@400;600;700;800&family=Yanone+Kaffeesatz:wght@400;500&display=swap">
<style>
:root{
  --blue:#1ea4da;
  --blue-dark:#1283b4;
  --orange:#f07a16;
  --green:#5fb34a;
  --purple:#a777d6;
  --navy:#1d3a5c;
  --ink:#333;
  --muted:#666;
  --line:#dcdcdc;
  --panel:#f4f4f4;
  --footer:#f1f1f1;
}
*{box-sizing:border-box;margin:0;padding:0}
html,body{width:680px;height:1200px;overflow:hidden;background:#fff}
body{position:relative;font-family:"Open Sans",Arial,sans-serif;color:var(--ink)}
.heading-font{font-family:"Yanone Kaffeesatz","Arial Narrow",sans-serif}

/* header */
.site-header{position:absolute;left:0;top:0;width:680px;height:52px;background:linear-gradient(#fff,#f3f3f3);border-bottom:1px solid #e4e4e4}
.brand{position:absolute;left:140px;top:14px;display:flex;align-items:center;gap:6px}
.brand-mark{width:14px;height:14px;background:var(--blue)}
.brand-name{font-weight:700;font-size:11px;line-height:11px;color:var(--blue);width:90px}
.main-nav{position:absolute;left:273px;top:22px;display:flex;font-size:6.5px;font-weight:700;color:#222}
.main-nav a{color:inherit;text-decoration:none;padding:4px 9px;border-radius:8px;line-height:6px}
.main-nav a.active{background:var(--blue);color:#fff}

/* hero */
.hero{position:absolute;left:0;top:52px;width:680px;height:200px;background:linear-gradient(90deg,#e9f1f6 0%,#dde9f0 30%,#c9b7a4 55%,#e3d6c8 75%,#eef2f4 100%)}
.hero-text{position:absolute;left:118px;top:40px;width:120px;text-align:right;color:var(--orange);font-weight:700;font-size:14.5px;line-height:19.5px}
.hero-cta{position:absolute;left:148px;top:136px;width:68px;height:24px;border-radius:12px;background:var(--orange);color:#fff;font-size:6.5px;font-weight:700;display:flex;align-items:center;justify-content:center;box-shadow:0 2px 3px rgba(0,0,0,.25);border:2px solid #fff}
.hero-dots{position:absolute;left:509px;top:185px;display:flex;gap:3px}
.hero-dots i{width:6px;height:6px;background:#fff}
.hero-dots i.on{background:#222}

/* intro */
.intro{position:absolute;left:150px;top:256px;width:380px;text-align:center;font-size:16px;line-height:20px;color:#333;font-weight:400}
.intro em{font-style:normal;color:var(--orange)}
.intro .u{border-bottom:1px solid #e8d9a0}

/* quick links */
.quick-links{position:absolute;left:140px;top:305px;display:flex}
.quick-link{width:68px;height:62px;text-align:center;background:linear-gradient(90deg,#fff 80%,#f2f2f2);font-size:5.8px;font-weight:700;line-height:8px;color:#222}
.quick-link svg{display:block;margin:6px auto 6px}

/* posts */
.section-title{position:absolute;left:140px;font-size:16px;color:#333;font-weight:400}
.post{position:absolute;left:140px;width:268px;height:66px}
.thumb{position:absolute;left:0;top:0;width:32px;height:32px;background:linear-gradient(#8ba0b0,#6b7a5a);border:1px solid #ccc}
.date{position:absolute;left:0;top:44px;width:34px;text-align:center;color:#555;font-size:5.5px;line-height:7px}
.date b{display:block;font-size:13px;line-height:15px;color:#444}
.post-body{position:absolute;left:35px;top:0;right:0;bottom:0;border:1px solid var(--line);border-radius:2px;background:#fff}
.post-body::before{content:"";position:absolute;left:0;right:0;top:0;height:19px;background:linear-gradient(#fff,#f1f1f1)}
.post-body h3{position:absolute;left:7px;top:7px;font-family:"Yanone Kaffeesatz","Arial Narrow",sans-serif;font-weight:500;font-size:11.5px;color:var(--blue);line-height:12px}
.count{position:absolute;right:10px;top:8px;width:18px;height:10px;border-radius:5px;background:#e6e6e6;font-size:5.5px;font-weight:700;text-align:center;line-height:10px}
.post-body p{position:absolute;left:7px;top:22px;width:210px;font-size:5.6px;line-height:9px;color:#444}
.post-body hr{position:absolute;left:7px;right:10px;top:43px;border:0;border-top:1px solid #eee}
.share{position:absolute;left:7px;top:49px;display:flex;gap:3px}
.share span{font-size:4.5px;border:1px solid #ccc;border-radius:2px;padding:1px 3px;background:#f7f7f7;color:#335}

/* sidebar */
.box{position:absolute;left:420px;width:122px;border:1px solid var(--line);border-radius:3px;background:#fafafa}
.box h4{font-family:"Yanone Kaffeesatz","Arial Narrow",sans-serif;font-weight:400;font-size:12.5px;color:#333;padding:7px 7px 0}
.policy-box{top:376px;height:70px;background:var(--navy);border-color:var(--navy)}
.policy-box h4{color:#fff;padding-top:3px}
.policy-form{position:absolute;left:5px;top:19px;width:107px;height:44px;background:#eef1f4}
.select{position:absolute;left:3px;width:101px;height:11px;background:#fff;border:1px solid #bbb;font-size:4.8px;color:#777;padding-left:4px;line-height:10px}
.select::after{content:"";position:absolute;right:0;top:0;width:11px;height:9px;background:var(--blue)}
.go{position:absolute;left:9px;top:63px;width:14px;height:12px;background:var(--blue);color:#fff;font-size:5px;text-align:center;line-height:12px;border-radius:1px}
.reviews{top:468px;height:124px}
.reviews ul{list-style:none;padding:8px 0 0 10px}
.reviews li{font-size:6px;color:#444;line-height:14.7px;display:flex;align-items:center;gap:7px}
.ad{top:600px;height:138px}
.ad-slot{position:absolute;left:7px;top:34px;width:108px;height:98px;background:#777}
.social{top:746px;height:136px}
.fb{position:absolute;left:8px;top:6px;width:106px;height:124px;background:#fff;border:1px solid #c9d0dc}
.fb-top{background:#eceff5;font-size:5px;font-weight:700;padding:3px 4px;color:#333;border-bottom:1px solid #c9d0dc}
.fb-page{position:absolute;left:4px;top:16px;width:20px;height:20px;background:var(--green)}
.fb-name{position:absolute;left:27px;top:16px;font-size:5.5px;font-weight:700;color:#3b5998;line-height:6px}
.fb-like{position:absolute;left:27px;top:30px;font-size:4.5px;border:1px solid #ccc;padding:0 3px;background:#f4f4f4}
.fb-count{position:absolute;left:4px;top:42px;font-size:4.5px;color:#444;width:100px;line-height:6px}
.fb-faces{position:absolute;left:4px;top:56px;display:grid;grid-template-columns:repeat(5,18px);gap:3px}
.fb-faces i{width:18px;height:18px;background:linear-gradient(#b8a597,#6f6a72)}
.tweets{top:892px;height:114px}
.tweet{padding:6px 8px 0;font-size:5.5px;color:#666;line-height:7.5px}
.tweet a{color:var(--blue);text-decoration:none;display:block}
.tweet small{font-size:4.3px;color:#999}
.tweet + .tweet{border-top:1px solid #e6e6e6;margin:6px 8px 0;padding:6px 0 0}

/* footer */
.site-footer{position:absolute;left:0;top:1030px;width:680px;height:144px;background:var(--footer);border-top:1px solid #e2e2e2}
.footer-art{position:absolute;left:130px;top:63px;width:60px;height:78px;background:linear-gradient(#c4c4c4,#e6e6e6);border-radius:20px 20px 4px 4px}
.fcol{position:absolute;top:24px;font-size:5.5px;color:#444}
.fcol h5{font-size:6px;font-weight:700;color:#222;margin-bottom:9px}
.fcol .tw{font-family:Georgia,serif;font-weight:700;font-size:5.5px;line-height:7px}
.fcol .link{color:#5a6fc0;font-size:5px;display:block;margin-top:3px}
.fcol small{font-size:4.3px;color:#999;display:block;margin-bottom:10px}
.contact{display:flex;gap:7px;align-items:flex-start;margin-bottom:8px;line-height:8px}
.contact svg{flex:none}
.pill{display:inline-block;font-size:4.5px;border:1px solid #bbb;background:#fff;padding:0 3px;margin-right:2px}
.sq{display:inline-block;width:7px;height:7px;vertical-align:middle;margin-right:2px}
.facts li{list-style:none;line-height:7.5px;margin-bottom:3px}
.bottom-bar{position:absolute;left:0;top:1174px;width:680px;height:26px;background:var(--blue);color:#fff;font-size:5.5px}
.bottom-bar .l{position:absolute;left:138px;top:10px}
.bottom-bar .r{position:absolute;left:371px;top:10px}
</style>
</head>
<body>

<header class="site-header">
  <div class="brand"><span class="brand-mark"></span><span class="brand-name">Furrow Cover Polls UK</span></div>
  <nav class="main-nav">
    <a class="active" href="#">HOME</a><a href="#">POLICIES</a><a href="#">GLOSSARY</a><a href="#">FACT SHEETS</a><a href="#">SURVEY REPORTS</a><a href="#">NEWS</a>
  </nav>
</header>

<section class="hero" role="img" aria-label="Slideshow photo of a family with their dog at home">
  <p class="hero-text">We do not sell pet insurance or receive commission…</p>
  <div class="hero-cta">GET STARTED</div>
  <div class="hero-dots"><i></i><i class="on"></i><i></i><i></i></div>
</section>

<h2 class="intro heading-font"><span class="u">Pet Insurance Policies <em>A-Z Listing</em> Click on any policy name to view</span><br><span class="u">the full policy details.</span></h2>

<nav class="quick-links">
  <a class="quick-link"><svg width="22" height="26" viewBox="0 0 22 26"><path d="M2 2h12l6 6v16H2z" fill="#5fb34a"/><path d="M14 2v6h6" fill="#3f8c2e"/></svg>POLICY FILES</a>
  <a class="quick-link"><svg width="24" height="26" viewBox="0 0 24 26"><circle cx="14" cy="9" r="7" fill="none" stroke="#2f6fa3" stroke-width="3"/><path d="M9 14L2 22" stroke="#2f6fa3" stroke-width="4"/></svg>POLICY SEARCH</a>
  <a class="quick-link"><svg width="22" height="26" viewBox="0 0 22 26"><rect x="2" y="3" width="18" height="22" rx="2" fill="#f07a16"/><rect x="7" y="1" width="8" height="4" fill="#c75f0c"/></svg>POLICY FILES</a>
  <a class="quick-link"><svg width="24" height="26" viewBox="0 0 24 26"><rect x="1" y="3" width="22" height="20" fill="#fff" stroke="#444" stroke-width="2"/><rect x="1" y="3" width="22" height="5" fill="#444"/><path d="M5 12h14M5 16h14M5 20h14" stroke="#777"/></svg>POLICY LISTINGS<br>BY TYPE</a>
  <a class="quick-link"><svg width="24" height="26" viewBox="0 0 24 26"><path d="M12 3a10 10 0 1 0 10 10H12z" fill="#1ea4da"/><path d="M14 1v10h10A10 10 0 0 0 14 1z" fill="#1283b4"/></svg>CLAIMS SURVEY</a>
  <a class="quick-link"><svg width="22" height="26" viewBox="0 0 22 26"><path d="M2 2h12l6 6v16H2z" fill="#a777d6"/><path d="M14 2v6h6" fill="#7f52ad"/></svg>PRICE SURVEY<br>REPORT</a>
</nav>

<h2 class="section-title heading-font" style="top:369px">Latest News</h2>

<article class="post" style="top:397px"><div class="thumb" role="img" aria-label="Author photo"></div><div class="date">December<b>30</b></div>
<div class="post-body"><h3>About Furrow Cover Polls.</h3><span class="count">10</span><p>Here are some of the best articles I've read over the last week. As always, if there's any great resources out there.</p><hr><div class="share"><span>Tweet</span><span>Like</span></div></div></article>

<article class="post" style="top:470px"><div class="thumb" role="img" aria-label="Author photo"></div><div class="date">December<b>30</b></div>
<div class="post-body"><h3>About Furrow Cover Polls.</h3><span class="count">10</span><p>I'm please to introduce Tom Ellery who will be contributing some articles here on Spread Desk Weekly. Take it away Tom.</p><hr><div class="share"><span>Tweet</span><span>Like</span></div></div></article>

<article class="post" style="top:543px"><div class="thumb" role="img" aria-label="Author photo"></div><div class="date">December<b>30</b></div>
<div class="post-body"><h3>About Furrow Cover Polls.</h3><span class="count">10</span><p>Double diagonals are not your average options strategy. Let's take a detailed look at this little known strategy.</p><hr><div class="share"><span>Tweet</span><span>Like</span></div></div></article>

<h2 class="section-title heading-font" style="top:621px">Latest Review</h2>

<article class="post" style="top:649px"><div class="thumb" role="img" aria-label="Author photo"></div><div class="date">December<b>30</b></div>
<div class="post-body"><h3>About Furrow Cover Polls.</h3><span class="count">10</span><p>Here are some of the best articles I've read over the last week. As always, if there's any great resources out there.</p><hr><div class="share"><span>Tweet</span><span>Like</span></div></div></article>

<article class="post" style="top:722px"><div class="thumb" role="img" aria-label="Author photo"></div><div class="date">December<b>30</b></div>
<div class="post-body"><h3>About Furrow Cover Polls.</h3><span class="count">10</span><p>I'm please to introduce Tom Ellery who will be contributing some articles here on Spread Desk Weekly. Take it away Tom.</p><hr><div class="share"><span>Tweet</span><span>Like</span></div></div></article>

<article class="post" style="top:796px"><div class="thumb" role="img" aria-label="Author photo"></div><div class="date">December<b>30</b></div>
<div class="post-body"><h3>About Furrow Cover Polls.</h3><span class="count">10</span><p>Double diagonals are not your average options strategy. Let's take a detailed look at this little known strategy.</p><hr><div class="share"><span>Tweet</span><span>Like</span></div></div></article>

<article class="post" style="top:869px"><div class="thumb" role="img" aria-label="Author photo"></div><div class="date">December<b>30</b></div>
<div class="post-body"><h3>The Ultimate Guide to Double Diagonal Spreads</h3><span class="count">10</span><p>Double diagonals are not your average options strategy. Let's take a detailed look at this little known strategy.</p><hr><div class="share"><span>Tweet</span><span>Like</span></div></div></article>

<article class="post" style="top:942px"><div class="thumb" role="img" aria-label="Author photo"></div><div class="date">December<b>30</b></div>
<div class="post-body"><h3>The Ultimate Guide to Double Diagonal Spreads</h3><span class="count">10</span><p>Double diagonals are not your average options strategy. Let's take a detailed look at this little known strategy.</p><hr><div class="share"><span>Tweet</span><span>Like</span></div></div></article>

<aside>
  <div class="box policy-box"><h4>Check out a Policy</h4>
    <div class="policy-form">
      <div class="select" style="top:4px">- Select Company -</div>
      <div class="select" style="top:21px">- Select Policy -</div>
    </div>
    <div class="go">Go</div>
  </div>

  <div class="box reviews"><h4>Popular Reviews</h4>
    <ul>
      <li><svg width="7" height="6" viewBox="0 0 7 6"><path d="M0 3l2.5 2.5L7 0" fill="none" stroke="#5fb34a" stroke-width="1.6"/></svg>Lorem ipsum dolor sit amet</li>
      <li><svg width="7" height="6" viewBox="0 0 7 6"><path d="M0 3l2.5 2.5L7 0" fill="none" stroke="#5fb34a" stroke-width="1.6"/></svg>Donec consequat imperdiet</li>
      <li><svg width="7" height="6" viewBox="0 0 7 6"><path d="M0 3l2.5 2.5L7 0" fill="none" stroke="#5fb34a" stroke-width="1.6"/></svg>Nam convallis bibendum elit</li>
      <li><svg width="7" height="6" viewBox="0 0 7 6"><path d="M0 3l2.5 2.5L7 0" fill="none" stroke="#5fb34a" stroke-width="1.6"/></svg>Sed sagittis purus augue</li>
      <li><svg width="7" height="6" viewBox="0 0 7 6"><path d="M0 3l2.5 2.5L7 0" fill="none" stroke="#5fb34a" stroke-width="1.6"/></svg>Nulla semper odio tempus</li>
      <li><svg width="7" height="6" viewBox="0 0 7 6"><path d="M0 3l2.5 2.5L7 0" fill="none" stroke="#5fb34a" stroke-width="1.6"/></svg>Donec consequat imperdiet</li>
    </ul>
  </div>

  <div class="box ad"><h4>Advertise Here</h4><div class="ad-slot" role="img" aria-label="Advertisement space"></div></div>

  <div class="box social">
    <div class="fb">
      <div class="fb-top">Find us on the social feed</div>
      <div class="fb-page"></div>
      <div class="fb-name">Furrow Cover<br>Polls UK</div>
      <div class="fb-like">Like</div>
      <div class="fb-count">211 people like Harbour Street Food Fair and others.</div>
      <div class="fb-faces" role="img" aria-label="Profile photos of followers"><i></i><i></i><i></i><i></i><i></i><i></i><i></i><i></i><i></i><i></i></div>
    </div>
  </div>

  <div class="box tweets"><h4>Pet Charities Latest Tweets</h4>
    <div class="tweet">Lorem Ipsum is dummy text of the text ever but the majority.<a>pawfund.net/item/website-r...</a><small>10 days ago</small></div>
    <div class="tweet">Lorem Ipsum is dummy text of the text ever but the majority.<a>pawfund.net/item/website-r...</a><small>10 days ago</small></div>
  </div>
</aside>

<footer class="site-footer">
  <div class="footer-art" role="img" aria-label="Silhouette of a dog and cat"></div>
  <div class="fcol" style="left:197px;width:90px">
    <h5>LATEST POSTS</h5>
    <div class="tw">Lorem Ipsum is simply the printing industry.</div><small>10 days ago</small>
    <div class="tw">Lorem Ipsum is simply the printing industry.</div><span class="link">pawfund.net/item/website-r...</span><small>10 days ago</small>
    <span class="link" style="color:#7a8ad0">View All »</span>
  </div>
  <div class="fcol" style="left:309px;width:120px">
    <h5>DON'T BE SHY...</h5>
    <div class="contact"><svg width="9" height="7" viewBox="0 0 9 7"><rect x=".5" y=".5" width="8" height="6" fill="none" stroke="#333"/><path d="M.5.5l4 3.5 4-3.5" fill="none" stroke="#333"/></svg><span style="color:#7a5fc0">info@furrowcoverpolls.co.uk</span></div>
    <div class="contact"><svg width="9" height="8" viewBox="0 0 9 8"><path d="M1 3C1 1 3 1 4.5 1S8 1 8 3L6.5 3.5 6 2.5H3L2.5 3.5zM2 4h5l1 3.5H1z" fill="#333"/></svg><span>Tel No. &nbsp;+44 20 7946 0318</span></div>
    <div class="contact"><svg width="9" height="9" viewBox="0 0 9 9"><rect x=".5" y=".5" width="8" height="8" fill="none" stroke="#333"/><path d="M4.5 2a1.7 1.7 0 0 1 1.7 1.7c0 1.3-1.7 3.3-1.7 3.3S2.8 5 2.8 3.7A1.7 1.7 0 0 1 4.5 2z" fill="#333"/></svg><span>6/8-10 Lorem Ipsum Place Name,<br>Country 123456</span></div>
    <h5 style="margin:10px 0 6px">SOCIAL WITH US</h5>
    <div><span class="sq" style="background:#3b5998"></span><span class="pill">Like</span><span class="pill">12k</span> &nbsp; <span class="sq" style="background:var(--blue)"></span><span class="pill">8 Followers</span></div>
  </div>
  <div class="fcol facts" style="left:450px;width:100px">
    <h5>POPULAR FACT SHEETS</h5>
    <ul>
      <li>» Pet Insurance - an introduction</li>
      <li>» Pet Insurance Policies -<br>&nbsp;&nbsp;&nbsp;Know Your Terms</li>
      <li>» Vet Fees - Policy Types</li>
      <li>» Using Price Comparison Engines</li>
      <li>» Common Policy Terms</li>
    </ul>
  </div>
</footer>

<div class="bottom-bar">
  <span class="l">Privacy Policy &nbsp;| &nbsp;Legal &nbsp;| &nbsp;About Furrow Cover Polls UK &nbsp;| &nbsp;News</span>
  <span class="r">Copyright © 2013 Furrow Cover Polls UK. All Rights Reserved.</span>
</div>

</body>
</html>
```